New Business Card Design Project

Hi! I would like for you to design a business card for our aesthetic injections business. We offer Zelvia, filler, skin care. I would like it to be elegant, feminine, modern and sleek/clean. I like black/gold foil/ivory/parchment colors. It can be either one or two sided. I would like matte black with gold foil logo on one side and ivory with gold foil information on the other side

Target Market(s)

target market is the discerning woman who wants to look her best

Industry/Entity Type

beauty

Contact Information for Business Card

logo, name, phone, email, website, instagram, facebook, location

Requirements
Must have
• logo and info
Nice to have
• the icons for cell, instagram, email, fb etc
Should not have
• images of people

```html
<!DOCTYPE html>
<html lang="en">
<head>
<meta charset="utf-8">
<title>The Velour Studio – Business Card</title>
<link href="https://fonts.googleapis.com/css2?family=Arimo:wght@400;700&display=swap" rel="stylesheet">
<style>
  :root {
    --backdrop: #d9d7d3;
    --card-black: #1e1e1e;
    --gold: #cfae55;
    --gold-soft: #b8963f;
  }
  html, body {
    margin: 0;
    padding: 0;
    width: 1200px;
    height: 866px;
    overflow: hidden;
    background: var(--backdrop);
    font-family: "Arimo", Arial, sans-serif;
  }
  .canvas {
    position: relative;
    width: 1200px;
    height: 866px;
  }
  .card {
    position: absolute;
    width: 520px;
    height: 297px;
    background: var(--card-black);
    border-bottom: 2px solid var(--gold-soft);
    box-sizing: border-box;
  }
  .card--front { left: 50px; top: 180px; }
  .card--back  { left: 630px; top: 390px; }

  .brand {
    position: absolute;
    width: 150px;
    height: 150px;
    border: 1.5px solid var(--gold);
    border-radius: 50%;
    display: flex;
    align-items: center;
    justify-content: center;
    text-align: center;
    box-sizing: border-box;
  }
  .brand__name {
    color: var(--gold);
    font-weight: 400;
    font-size: 17px;
    letter-spacing: 2px;
    line-height: 1.35;
    text-transform: uppercase;
  }
  .card--front .brand { left: 185px; top: 73px; }
  .card--back .brand  { left: 50px; top: 73px; }

  .divider {
    position: absolute;
    left: 240px;
    top: 70px;
    width: 1px;
    height: 157px;
    background: var(--gold);
  }
  .contact {
    position: absolute;
    left: 262px;
    top: 62px;
    color: var(--gold);
    font-size: 12px;
    line-height: 1.45;
  }
  .contact__name {
    font-weight: 700;
    font-size: 16px;
    letter-spacing: 0.5px;
    text-transform: uppercase;
  }
  .contact__role { margin-bottom: 12px; }
  .contact__address { margin-bottom: 8px; }
  .contact__list { list-style: none; margin: 0; padding: 0; }
  .contact__list li {
    display: flex;
    align-items: center;
    gap: 6px;
    height: 17px;
  }
  .icon { width: 10px; height: 10px; flex: none; }
  .icon--plain {
    width: 9px;
    height: 9px;
    background: var(--gold);
    border-radius: 1px;
  }
</style>
</head>
<body>
<div class="canvas">

  <section class="card card--front" aria-label="Business card front">
    <div class="brand"><span class="brand__name">The<br>Velour<br>Studio</span></div>
  </section>

  <section class="card card--back" aria-label="Business card back">
    <div class="brand"><span class="brand__name">The<br>Velour<br>Studio</span></div>
    <div class="divider"></div>
    <div class="contact">
      <div class="contact__name">Marcus Hale</div>
      <div class="contact__role">Operations Manager</div>
      <div class="contact__address">48 Willow Crest Lane,<br>Maple Grove, ON L6A 3K2</div>
      <ul class="contact__list">
        <li>
          <svg class="icon" viewBox="0 0 10 10" aria-hidden="true"><path d="M2 0.8 L3.6 0.8 L4.2 3 L3.1 3.9 Q4.2 6 6.1 6.9 L7 5.8 L9.2 6.4 L9.2 8 Q8.6 9.4 7 9.2 Q1 7.8 0.8 2.2 Q0.8 0.9 2 0.8Z" fill="#cfae55"/></svg>
          905-555-0147
        </li>
        <li>
          <svg class="icon" viewBox="0 0 10 10" aria-hidden="true"><rect x="0.5" y="2" width="9" height="6.5" fill="#cfae55"/><path d="M0.8 2.3 L5 5.6 L9.2 2.3" stroke="#1e1e1e" stroke-width="0.9" fill="none"/></svg>
          hello@velourstudio.ca
        </li>
        <li>
          <svg class="icon" viewBox="0 0 10 10" aria-hidden="true"><circle cx="5" cy="5" r="4.3" stroke="#cfae55" stroke-width="1" fill="none"/><ellipse cx="5" cy="5" rx="1.8" ry="4.3" stroke="#cfae55" stroke-width="0.8" fill="none"/><line x1="0.7" y1="5" x2="9.3" y2="5" stroke="#cfae55" stroke-width="0.8"/></svg>
          www.velourstudio.ca
        </li>
        <li><span class="icon icon--plain"></span>@thevelourstudio</li>
        <li><span class="icon icon--plain"></span>@thevelourstudio</li>
      </ul>
    </div>
  </section>

</div>
</body>
</html>
```